updated documents

Hi i have included a new picture for the about us section, i have also included the updated word document, all changes have been highlighted.

Thanks,

Leon

```html
<!DOCTYPE html>
<html lang="en">
<head>
<meta charset="utf-8">
<title>About Us – Tidewell Property Services</title>
<link href="https://fonts.googleapis.com/css2?family=Titillium+Web:wght@300;400&display=swap" rel="stylesheet">
<style>
  :root {
    --page: #ffffff;
    --ink: #5a5a5a;
    --title: #555555;
    --accent: #9bc31c;
    --icon: #8c8c8c;
    --shadow: rgba(120, 150, 175, 0.45);
  }
  * { box-sizing: border-box; margin: 0; padding: 0; }
  html, body { width: 1200px; height: 852px; overflow: hidden; background: var(--page); }
  body { font-family: "Titillium Web", sans-serif; font-weight: 300; color: var(--ink); }
  .page { position: relative; width: 1200px; height: 852px; }

  .page-title {
    position: absolute; left: 50px; top: 36px;
    font-weight: 400; font-size: 29px; color: var(--title); letter-spacing: 0.3px;
  }
  .title-rule {
    position: absolute; left: 50px; top: 79px; width: 515px; height: 2px; background: var(--accent);
  }
  .intro {
    position: absolute; left: 50px; top: 92px; width: 516px;
    font-size: 11.2px; line-height: 14.4px; text-align: justify;
  }
  .intro p + p { margin-top: 14px; }

  .service { position: absolute; width: 442px; font-size: 11.2px; line-height: 14.4px; text-align: justify; }
  .service h2 { font-weight: 400; font-size: 12.6px; line-height: 15px; color: var(--accent); text-align: left; }
  .left .service { left: 133px; }
  .right .service { left: 713px; }

  .badge {
    position: absolute; width: 64px; height: 64px; border-radius: 50%;
    background: var(--page);
    box-shadow: -7px 9px 10px -3px var(--shadow);
    display: flex; align-items: center; justify-content: center;
  }
  .badge svg { width: 58px; height: 58px; fill: var(--icon); }
  .left .badge { left: 46px; }
  .right .badge { left: 624px; }

  .building-visual {
    position: absolute; left: 884px; top: 542px; width: 280px; height: 275px;
    background: radial-gradient(ellipse at 55% 45%, #cfcfcf 0%, #e4e4e4 45%, #f6f6f6 75%, #ffffff 100%);
    border-radius: 8px;
  }
</style>
</head>
<body>
<main class="page">
  <h1 class="page-title">About Us</h1>
  <div class="title-rule"></div>
  <section class="intro">
    <p>Tidewell Property Services is an Adelaide based company providing general building and office maintenance and refurbishments. We pride ourselves in delivering cost affective high quality services with minimal disturbance to tenants and their occupants.</p>
    <p>Tidewell Property Services provides a wide range of services including all major trades Electrical, Data, Plumbing, carpentry, landscaping, and more. With all trades available we can manage their work as required. We also provide preventive maintenance programs to help reduce future reactive works. Our Team are have all undertaken police checks and are white card accredited.</p>
  </section>

  <div class="left">
    <div class="badge" style="top:220px"><svg viewBox="0 0 60 60"><path d="M26 4h8l1.5 7 5 2 6-4 5.5 5.5-4 6 2 5 7 1.5v8l-7 1.5-2 5 4 6-5.5 5.5-6-4-5 2L34 56h-8l-1.5-7-5-2-6 4-5.5-5.5 4-6-2-5L4 34v-8l7-1.5 2-5-4-6L14.5 8l6 4 5-2zM30 21a9 9 0 1 0 0 18 9 9 0 0 0 0-18z"/></svg></div>
    <article class="service" style="top:218px"><h2>Building Repairs and Maintenance</h2><p>The team at Tidewell Property Services have extensive skills and experience in both internal and external building repairs and maintenance. Installation and repairs to floor and ceilings systems, doors/locks, appliance repairs, whiteboards, TV screens, picture hanging, patching and paint, vandal repairs, workstations and joinery, plumbing and electrical.</p></article>

    <div class="badge" style="top:308px"><svg viewBox="0 0 60 60"><path d="M30 2a28 28 0 1 1 0 56 28 28 0 0 1 0-56zm0 5a23 23 0 1 0 0 46 23 23 0 0 0 0-46z"/><rect x="22" y="12" width="4" height="10"/><rect x="34" y="12" width="4" height="10"/><path d="M18 22h24v8a12 12 0 0 1-9 11.6V50h-6v-8.4A12 12 0 0 1 18 30z"/></svg></div>
    <article class="service" style="top:311px"><h2>Electrical</h2><p>Tidewell Property Services provides a wide range of electrical services ranging from Test and tag, Mains services, Switchboard installations, fault finding, RCD testing, data cabling/patching, electrical upgrades and lighting.</p></article>

    <div class="badge" style="top:398px"><svg viewBox="0 0 60 60"><path d="M8 40a22 22 0 0 1 44 0zM4 42h52v6H4z"/></svg></div>
    <article class="service" style="top:396px"><h2>Planned Preventative Maintenance</h2><p>Tidewell Property Services Offer planned preventive maintenance specifically tailored to the client's requirements. Planned maintenance schedules can be created to prevent breakdowns and costly reactive maintenance in the future. Maintenance programs can include floor and ceiling repairs, light bulb replacements, Test and tagging, Storm water and gutter cleaning.</p></article>

    <div class="badge" style="top:483px"><svg viewBox="0 0 60 60"><path d="M36 6l14 14-10 10-14-14z"/><path d="M25 19l12 12-6 6-12-12z"/><path d="M19 27l10 10-12 14c-3 3-8 1-10-1s-4-7-1-10z"/></svg></div>
    <article class="service" style="top:497px"><h2>Painting</h2><p>Tidewell Property Services pride ourselves in quality and detail ensuring the very best results while being a cost effective and efficient.</p></article>

    <div class="badge" style="top:572px"><svg viewBox="0 0 60 60"><rect x="8" y="8" width="5" height="48"/><rect x="13" y="14" width="38" height="4"/><rect x="17" y="20" width="34" height="20"/></svg></div>
    <article class="service" style="top:580px"><h2>Signage</h2><p>Tidewell Property Services have an experience signage team that specialize in both internal and external signage, decals, promotional banners, window frosting, company logos and design.</p></article>

    <div class="badge" style="top:660px"><svg viewBox="0 0 60 60"><path d="M8 12h44v36H8zm3 3v30h38V15z"/><rect x="14" y="18" width="8" height="6"/><rect x="26" y="18" width="10" height="10"/><rect x="40" y="18" width="6" height="12"/><rect x="14" y="30" width="6" height="10"/><rect x="24" y="34" width="12" height="6"/><rect x="40" y="34" width="6" height="8"/></svg></div>
    <article class="service" style="top:666px"><h2>Office Layout Changes</h2><p>If you are looking to make some changes to your office either big or small our team can assist with Workstation reconfiguration, internal demolition, Partition/wall installations and even complete office relocations.</p></article>

    <div class="badge" style="top:746px"><svg viewBox="0 0 60 60"><path d="M14 8l8 8-3 3 24 24 3-3 6 6-6 6-6-6 3-3-24-24-3 3-8-8z"/><path d="M44 6a10 10 0 0 0-9 13L10 44a4 4 0 0 0 6 6l25-25a10 10 0 0 0 13-9l-6 4-6-2-2-6z"/></svg></div>
    <article class="service" style="top:758px"><h2>Appliance Repairs</h2><p>Tidewell Property Services can repair and replace all of your office appliance's ranging from dishwashers and microwaves to monitors, TV's and projectors.</p></article>
  </div>

  <div class="right">
    <div class="badge" style="top:46px"><svg viewBox="0 0 60 60"><rect x="40" y="4" width="4" height="30"/><path d="M34 34h16l3 18H31z"/><path d="M8 30h24v22H8z"/><path d="M12 30a8 8 0 0 1 16 0h-3a5 5 0 0 0-10 0z"/></svg></div>
    <article class="service" style="top:56px"><h2>Cleaning</h2><p>Our team offer both internal and external cleaning services including carpark cleaning, window cleaning, carpet dry cleaning, and general office cleaning.</p></article>

    <div class="badge" style="top:134px"><svg viewBox="0 0 60 60"><path d="M24 6h12l7 12 4-2-4 12-12-2 4-2-5-9-5 9-7-4z"/><path d="M8 36l6 -11 7 4-5 9h10v-5l8 10-8 10v-5H14c-5 0-8-6-6-12z"/><path d="M52 36c2 6-1 12-6 12h-8v-8h9l-5-9 7-4z"/></svg></div>
    <article class="service" style="top:131px"><h2>Rubbish Removal/Recycling</h2><p>Tidewell Property Services specialize in office rubbish removal, We have a solution to all your rubbish removal needs; including, electronic waste recycling (PCs, monitors, printers, cables etc.), Basement access skip bins, wheelie bins of various sizes, internal demolition services, workstation/furniture removal, rubbish removal/cleanup services.</p></article>

    <div class="badge" style="top:220px"><svg viewBox="0 0 60 60"><rect x="24" y="2" width="6" height="12"/><path d="M18 14h16v6H26v14h28v8H18z"/><rect x="34" y="28" width="4" height="6"/><rect x="30" y="26" width="12" height="3"/><rect x="40" y="42" width="5" height="6"/><path d="M42.5 50l3 5a3 3 0 0 1-6 0z"/></svg></div>
    <article class="service" style="top:218px"><h2>Plumbing</h2><p>Our Plumbing team are experienced and available 24/7 for all your plumbing requirements. Our plumbing services include, water boiler/chiller unit installs and repairs, blocked drains and toilets, roof work and gas fitting.</p></article>

    <div class="badge" style="top:308px"><svg viewBox="0 0 60 60"><path d="M8 10l3-2 18 22-3 2z"/><path d="M20 32h22l8 8v4H20z"/><circle cx="24" cy="47" r="5"/><circle cx="48" cy="47" r="4"/></svg></div>
    <article class="service" style="top:308px"><h2>Grounds Keeping</h2><p>Let us help with your grounds keeping, our services include, lawn mowing and garden care, carpark sweeping, tree pruning, line marking, gutter cleaning, landscaping, bird and pest management, fencing installs and repairs.</p></article>

    <div class="badge" style="top:396px"><svg viewBox="0 0 60 60"><path d="M8 38h44v12H8z"/><path d="M18 14l8 14-4 2-8-14z"/><path d="M36 10l4 2-10 20-4-2z"/><path d="M42 18l8 4-6 12-8-4z"/><rect x="12" y="32" width="36" height="4"/></svg></div>
    <article class="service" style="top:403px"><h2>Carpentry</h2><p>Tidewell Property Services have a dedicated carpentry team that can assist with all your requirements including Partitioning, cupboard installations and all repairs and modifications.</p></article>

    <div class="badge" style="top:482px"><svg viewBox="0 0 60 60"><path d="M6 30l9-5 8 5-9 5z"/><path d="M20 23l9-5 8 5-9 5z"/><path d="M34 16l9-5 8 5-9 5z"/><path d="M23 38l9-5 8 5-9 5z"/><path d="M37 31l9-5 8 5-9 5z"/><path d="M26 32l4-2 4 2-4 2z"/></svg></div>
    <article class="service" style="top:487px"><h2>Floor/Ceiling</h2><p>We can provide floor and ceiling repairs to all types of systems including, suspended ceiling systems and raised floors, ceiling/floor tile replacement, carpet and vinyl replacements and repairs, ceiling access hatches and air vent installs.</p></article>
  </div>

  <div class="building-visual" role="img" aria-label="Illustration of a multi-storey building under construction with a tower crane, resting on architectural plans with a calculator and charts"></div>
</main>
</body>
</html>
```